Brightvale services brochure

We need a new company brochure. The brochure will be formatted for PDF distribution but should be printable on "letter" size paper. 2 pages plus front and back cover. Color white and same blue as logo. Logo "O" should be used as design. Look at webpage for general info: www.brightvale-example.ca<br/><br/>Front cover: pic1, logo, design and "Your Cleaning is Our Business". <br/>Back cover" "O" design, logo and info from "contact" page<br/>Front cover inside: design and intro from web home page, also use stock pics of clean offices ect as placeholders for purchased pics.<br/>1st page: design and "Our Services", use info of "Cleanroom & GMP Services", "Janitorial Services" from services page.<br/>2nd page: design and "Special Services", info from "Carpet & Upholstery Services", "Window Cleaning Services", and list of "Other Services".<br/>Back cover inside : design and info from technology page, use stock pics for place holders.

Industry/Entity Type

Janitorial

Font styles to use
Sans Serif
Other font styles liked:
• Futura Book

Colors
0555a3

Requirements
Must have
• The logo "O" (target) should be part of the design. Design color same as logo.

```html
<!DOCTYPE html>
<html lang="en">
<head>
<meta charset="utf-8">
<title>Brightvale Building Services – Brochure</title>
<link rel="stylesheet" href="https://fonts.googleapis.com/css2?family=Poppins:wght@400;500;600;700;800&display=swap">
<style>
  :root{
    --brand:#0555a3;
    --brand-bright:#0a63b8;
    --navy:#0b2f5e;
    --deep:#123f77;
    --mid:#2f6fb5;
    --soft:#5b8fcb;
    --sky:#dfeaf5;
    --paper:#f4f5f7;
    --ink:#1d3557;
    --white:#ffffff;
    --stage:#e4e4e4;
  }
  *{box-sizing:border-box;margin:0;padding:0}
  html,body{width:869px;height:1200px;overflow:hidden}
  body{background:var(--stage);font-family:"Poppins",Arial,sans-serif;color:var(--ink);position:relative}

  .spread{position:absolute;left:0;width:869px;height:562px;display:flex;overflow:hidden;box-shadow:0 4px 14px rgba(0,0,0,.18)}
  .spread--covers{top:18px}
  .spread--inside{top:620px}
  .page{position:relative;width:434.5px;height:562px;overflow:hidden}
  .spread-deco{position:absolute;inset:0;pointer-events:none}

  /* covers */
  .back-cover{background:linear-gradient(160deg,var(--deep),var(--navy))}
  .back-cover .photo{position:absolute;left:40px;top:150px;width:330px;height:240px;background:linear-gradient(180deg,rgba(60,110,170,.35),rgba(20,60,110,.15));opacity:.8}
  .contact{position:absolute;left:34px;top:405px;color:var(--white);width:230px;z-index:1}
  .contact__intro{font-size:9.5px;line-height:1.35}
  .contact__quote{font-size:9.5px;font-weight:700;font-style:normal;padding:4px 0 6px;border-top:1px solid rgba(255,255,255,.6);margin-top:5px}
  .contact__list{list-style:none;font-size:11px;line-height:1.45;border-top:1px solid rgba(255,255,255,.6);padding-top:4px}
  .contact__list li{display:flex;align-items:center;gap:8px}
  .contact__list svg{width:10px;height:10px;flex:none}

  .front-cover{background:linear-gradient(180deg,#eaf1f9 0%,var(--sky) 30%,#c9dbee 100%)}
  .logo{display:flex;align-items:center;gap:6px;color:var(--brand);font-weight:500;letter-spacing:3px;white-space:nowrap}
  .logo__dot{width:9px;height:9px;border-radius:50%;background:var(--brand)}
  .front-cover .logo{position:absolute;right:36px;top:40px;font-size:17px}
  .headline{position:absolute;right:30px;top:78px;text-align:right;color:var(--brand-bright);font-weight:800;font-size:27px;line-height:1.1;text-transform:uppercase}
  .front-cover .photo{position:absolute;left:0;right:0;top:170px;bottom:0;background:linear-gradient(180deg,#dfe8f1 0%,#a9bccd 45%,#7f93a4 80%,#5e6a60 100%)}

  /* inside */
  .inside-left{background:var(--paper)}
  .inside-right{background:var(--paper)}
  .snap{position:absolute;border:4px solid var(--white);background:linear-gradient(135deg,#cfdbe6,#8fa6bb);box-shadow:0 1px 4px rgba(0,0,0,.25)}
  .intro{position:absolute;left:24px;top:300px;width:390px;font-size:6.6px;line-height:1.45;font-style:italic;color:#2b3a4f}
  .inside-left .logo{position:absolute;right:30px;top:334px;font-size:20px}
  .features{position:absolute;left:24px;top:374px;width:390px;display:grid;grid-template-columns:1fr 1fr;gap:14px 22px}
  .feature{display:flex;gap:8px}
  .feature svg{width:20px;height:20px;flex:none;fill:var(--brand)}
  .feature h3{font-size:7.5px;font-weight:700;color:var(--brand);text-transform:uppercase;font-style:italic}
  .feature p{font-size:6.4px;line-height:1.4;font-style:italic;color:#2b3a4f}

  .services-title{position:absolute;right:26px;top:50px;font-size:31px;font-weight:800;color:var(--brand-bright)}
  .services-rule{position:absolute;right:26px;top:96px;width:200px;height:2px;background:var(--brand)}
  .services{position:absolute;top:108px;left:22px;right:18px;display:grid;grid-template-columns:1fr 1fr;gap:0 14px}
  .service{display:flex;gap:7px;margin-bottom:9px}
  .service svg{width:20px;height:20px;flex:none;fill:var(--brand)}
  .service h3{font-size:7px;font-weight:700;color:var(--brand);text-transform:uppercase}
  .service p{font-size:5.8px;line-height:1.4;color:#2b3a4f}

  .offers-band{position:absolute;left:0;right:0;top:250px;height:106px;background:var(--brand)}
  .offers-title{position:absolute;left:40px;top:256px;color:var(--white);font-size:25px;font-weight:800}
  .offers{position:absolute;left:22px;top:296px;display:flex;gap:8px}
  .offer{width:92px;height:70px;border-radius:9px;color:var(--white);display:flex;flex-direction:column;justify-content:center;align-items:center;text-align:center;line-height:1.1}
  .offer small{font-size:8px}
  .offer strong{font-size:21px;font-weight:800}
  .offer--light{background:var(--soft)}
  .offer--dark{background:var(--navy)}
</style>
</head>
<body>

<section class="spread spread--covers" aria-label="Back and front cover">
  <div class="page back-cover">
    <div class="photo" role="img" aria-label="Faded photo of office towers"></div>
    <div class="contact">
      <p class="contact__intro">At Brightvale we are available 24/7 for supporting our clients.</p>
      <p class="contact__quote">“Your Cleaning is Our Business!”</p>
      <ul class="contact__list">
        <li><svg viewBox="0 0 10 10"><path fill="#fff" d="M2 0l2 2-1 1.5c.6 1.3 1.7 2.4 3 3L7.5 5.5l2 2L8 9.5C4 9.5.5 6 .5 2z"/></svg>1 (800) 555-0142</li>
        <li><svg viewBox="0 0 10 10"><rect x="1" y="3" width="8" height="5" fill="#fff"/><rect x="2.5" y="1" width="5" height="2" fill="#fff"/></svg>(555) 010-4477</li>
        <li><svg viewBox="0 0 10 10"><rect x="0.5" y="2" width="9" height="6" fill="#fff"/><path d="M.5 2l4.5 3.5L9.5 2" stroke="#123f77" fill="none"/></svg>info@brightvale-example.ca</li>
        <li><svg viewBox="0 0 10 10"><rect x="1" y="1" width="8" height="8" fill="none" stroke="#fff"/></svg>Social Page</li>
        <li><svg viewBox="0 0 10 10"><circle cx="5" cy="5" r="4" fill="none" stroke="#fff"/></svg>Network Page</li>
      </ul>
    </div>
  </div>
  <div class="page front-cover">
    <div class="logo"><span class="logo__dot"></span>BRIGHTVALE</div>
    <h1 class="headline">Your Cleaning is<br>Our Business</h1>
    <div class="photo" role="img" aria-label="Photo of a modern glass office building"></div>
  </div>
  <svg class="spread-deco" viewBox="0 0 869 562" aria-hidden="true">
    <path d="M330 562 C250 430 290 230 470 150" fill="none" stroke="#0a57a6" stroke-width="62" opacity=".9"/>
  </svg>
</section>

<section class="spread spread--inside" aria-label="Inside pages">
  <div class="page inside-left">
    <svg class="spread-deco" viewBox="0 0 434.5 562" aria-hidden="true">
      <path d="M0 0H434.5V150C330 160 200 220 0 290Z" fill="#0e3a70"/>
      <path d="M0 0H160L40 290H0Z" fill="#1d4d85" opacity=".7"/>
    </svg>
    <div class="snap" role="img" aria-label="Photo of a gloved hand wiping an office desk" style="left:230px;top:40px;width:130px;height:90px;transform:rotate(-18deg)"></div>
    <div class="snap" role="img" aria-label="Photo of a floor being machine polished" style="left:250px;top:150px;width:120px;height:90px;transform:rotate(-18deg)"></div>
    <div class="snap" role="img" aria-label="Photo of cleaners wiping office desks" style="left:110px;top:180px;width:120px;height:90px;transform:rotate(-18deg)"></div>
    <p class="intro">Brightvale, a Janitorial Services Company that has been in business since 1985, takes pride in providing the highest possible quality of janitorial and complete cleaning services for any type of operation. Brightvale provides services to clients across the region and many areas across the country.</p>
    <div class="logo"><span class="logo__dot"></span>BRIGHTVALE</div>
    <div class="features">
      <div class="feature"><svg viewBox="0 0 20 20"><path d="M10 18L2 9.5C-.5 6.5 2 2 5.5 2 7.5 2 9 3.5 10 5 11 3.5 12.5 2 14.5 2 18 2 20.5 6.5 18 9.5Z"/></svg><div><h3>Health &amp; Safety</h3><p>Brightvale exceeds all Provincial and Federal Health and Safety standards.</p></div></div>
      <div class="feature"><svg viewBox="0 0 20 20"><rect x="4" y="9" width="12" height="9" rx="1"/><path d="M6.5 9V6a3.5 3.5 0 0 1 7 0v3" fill="none" stroke="#0555a3" stroke-width="2"/></svg><div><h3>Security</h3><p>We screen, bond and insure all our employees to keep our clients and their premises safe.</p></div></div>
      <div class="feature"><svg viewBox="0 0 20 20"><rect x="1" y="6" width="18" height="12" rx="1.5"/><path d="M7 6V3.5h6V6" fill="none" stroke="#0555a3" stroke-width="2"/></svg><div><h3>Professionalism</h3><p>We apply GMP and industry best practices to ensure the highest possible quality of service.</p></div></div>
      <div class="feature"><svg viewBox="0 0 20 20"><path d="M2 10l5 5L18 4" fill="none" stroke="#0555a3" stroke-width="3"/></svg><div><h3>Quality Control System</h3><p>We utilize the latest technology in Quality Control, HR and Payroll systems to maximize our efficiency and better control our processes.</p></div></div>
    </div>
  </div>

  <div class="page inside-right">
    <svg class="spread-deco" viewBox="0 0 434.5 562" aria-hidden="true">
      <path d="M0 0H200C140 10 60 30 0 70Z" fill="#0e3a70"/>
      <path d="M0 70C60 30 140 10 200 0H260C160 20 70 50 0 110Z" fill="#2f6fb5"/>
      <path d="M434.5 562V440C360 480 280 530 200 562Z" fill="#0555a3"/>
    </svg>
    <h2 class="services-title">Our Services</h2>
    <div class="services-rule"></div>
    <div class="services">
      <div>
        <div class="service"><svg viewBox="0 0 20 20"><circle cx="8" cy="4" r="3"/><rect x="5" y="8" width="6" height="11"/><rect x="13" y="10" width="6" height="9"/></svg><div><h3>Janitorial Services</h3><p>Brightvale provides complete janitorial services for any type of operation, serving both public and private sectors.</p></div></div>
        <div class="service"><svg viewBox="0 0 20 20"><circle cx="10" cy="4" r="3"/><rect x="7" y="8" width="6" height="8"/><circle cx="5" cy="17" r="2.5"/></svg><div><h3>Carpet &amp; Upholstery Services</h3><p>Brightvale provides a full upholstery cleaning service.</p></div></div>
        <div class="service"><svg viewBox="0 0 20 20"><circle cx="12" cy="5" r="3"/><path d="M2 18h16v-4H8l-2-4H2z"/></svg><div><h3>Fire and Flood Restoration Services</h3><p>Brightvale can provide full Fire and Flood Restoration services.</p></div></div>
      </div>
      <div>
        <div class="service"><svg viewBox="0 0 20 20"><circle cx="8" cy="4" r="3"/><rect x="5" y="8" width="6" height="11"/><rect x="15" y="2" width="2" height="17"/></svg><div><h3>Cleanroom &amp; GMP Services</h3><p>Brightvale is a leading Cleanroom and GMP services company with an impressive performance record.</p></div></div>
        <div class="service"><svg viewBox="0 0 20 20"><rect x="9" y="2" width="10" height="10" fill="none" stroke="#0555a3" stroke-width="2"/><circle cx="5" cy="6" r="3"/><rect x="2" y="10" width="6" height="9"/></svg><div><h3>Window Cleaning Services</h3><p>Brightvale can tackle both high-rise and low-level window cleaning.</p></div></div>
        <div class="service"><svg viewBox="0 0 20 20"><rect x="2" y="7" width="6" height="11" rx="1"/><rect x="11" y="4" width="7" height="14" rx="1"/></svg><div><h3>Sanitation Supplies</h3><p>Brightvale supplies the highest quality janitorial supplies; contact us for a full list of supplies in stock.</p></div></div>
      </div>
    </div>

    <div class="offers-band"></div>
    <h2 class="offers-title">Our Special Offers</h2>
    <div class="offers">
      <div class="offer offer--light"><small>All<br>Estimates</small><strong>FREE</strong></div>
      <div class="offer offer--dark"><small>New Janitorial<br>Contracts</small><strong>FREE</strong></div>
      <div class="offer offer--light"><small>Janitorial<br>Supplies</small><strong>FREE</strong></div>
      <div class="offer offer--dark"><small>Starting<br>at</small><strong>$95</strong></div>
    </div>

    <div class="snap" role="img" aria-label="Photo of a gloved hand wiping an office desk" style="left:30px;top:390px;width:110px;height:80px;transform:rotate(-15deg);border-color:var(--brand)"></div>
    <div class="snap" role="img" aria-label="Photo of a floor being machine polished" style="left:150px;top:420px;width:110px;height:80px;transform:rotate(-15deg);border-color:var(--brand)"></div>
    <div class="snap" role="img" aria-label="Photo of cleaners wiping office desks" style="left:270px;top:410px;width:110px;height:80px;transform:rotate(-15deg);border-color:var(--brand)"></div>
  </div>
</section>

</body>
</html>
```